Global Expert Network Firm needs business card design

We need business card design for a new company based in Seoul, South Korea called 'Corwell Insight Partners'. We recruit industry experts covering all countries and connect our client and recruited expert by phone, face-to-face meetings and etc. We are a global expert network firm that is focused on delivering high-quality experts to our clients throughout the world. Our clients include multinational corporations, global consulting firms, private equity firms, venture capital firms, asset management companies.
We have made new logo and please find attachment.(Please use new logo)
Target Market(s)
Global Consulting Firms, Investment Firms, Private Equity Firms, Venture Capital Firms.
Industry/Entity Type
Recruitment
Contact Information for Business Card
We need two Languages (English and Korean Version).
The front is Korean and the back is English version.
[The back] [English]
Company Name: Corwell Insight Partners, Inc.
CEO Name: Daniel Park
Address: #507, Hanbit Bldg, 82 Maebongsan-ro, Dobong-gu, Seoul, 01327, Korea
Tel. +82 2 718 4052
Fax. +82 2 864 1097
Mobile. +82 10 7264 8815
Email: daniel@corwellip.com
Web: www.corwellip.com
[The front] [Korean] => Described in same order as English version.
회사명: 코웰인사이트파트너스(주)
대표이사: 박도현
주소: 서울시 도봉구 매봉산로 82 한빛빌딩 507호
Tel. 02 718 4052
Fax. 02 864 1097
Mobile. 010 7264 8815
Web: www.corwellip.com
Look and feel
Each slider illustrates characteristics of the customer's brand and the style your logo design should communicate.

```html
<!DOCTYPE html>
<html lang="ko">
<head>
<meta charset="utf-8">
<title>Corwell Insight Partners — Business Cards</title>
<link href="https://fonts.googleapis.com/css2?family=Marcellus&family=Marcellus+SC&family=Noto+Sans+KR:wght@400&display=swap" rel="stylesheet">
<style>
  :root {
    --backdrop: #d8dadf;
    --card: #1f2558;
    --ink: #f4f5fa;
    --rule: rgba(244, 245, 250, 0.85);
  }
  * { box-sizing: border-box; margin: 0; padding: 0; }
  html, body {
    width: 1200px; height: 900px; overflow: hidden;
    background: var(--backdrop);
  }
  .sheet {
    width: 1200px; height: 900px;
    display: flex; flex-direction: column;
    align-items: center; justify-content: center; gap: 40px;
  }
  .card {
    position: relative;
    width: 660px; height: 380px;
    background: var(--card);
    color: var(--ink);
    box-shadow: 0 10px 30px rgba(20, 24, 50, 0.25);
  }
  .card__rule {
    position: absolute; left: 36px; top: 40px; bottom: 40px;
    width: 1px; background: var(--rule);
  }
  .card__person {
    position: absolute; left: 52px; top: 40px;
    font-size: 27px; line-height: 1.15; font-weight: 400;
  }
  .card__contacts {
    position: absolute; left: 52px; bottom: 40px;
    font-size: 12.5px; line-height: 1.7;
  }
  .contact-line { display: flex; align-items: center; gap: 6px; white-space: nowrap; }
  .contact-line .gap { width: 8px; }
  .icon { width: 12px; height: 12px; fill: var(--ink); flex: none; }
  .brand {
    position: absolute; right: 40px; top: 150px;
    display: flex; align-items: center; gap: 12px;
    font-size: 26px; line-height: 1; font-weight: 400;
    color: var(--ink); white-space: nowrap;
  }
  .brand__mark {
    width: 14px; height: 14px; background: var(--ink); flex: none;
  }
  .card--ko { font-family: "Marcellus", "Noto Sans KR", serif; }
  .card--ko .card__person { font-family: "Noto Sans KR", sans-serif; }
  .card--en { font-family: "Marcellus SC", serif; }
  .card--en .card__contacts { font-size: 13px; }
</style>
</head>
<body>
<svg width="0" height="0" style="position:absolute">
  <defs>
    <symbol id="i-phone" viewBox="0 0 24 24"><path d="M6.6 10.8a15 15 0 0 0 6.6 6.6l2.2-2.2a1 1 0 0 1 1-.25 11.4 11.4 0 0 0 3.6.57 1 1 0 0 1 1 1V20a1 1 0 0 1-1 1A17 17 0 0 1 3 4a1 1 0 0 1 1-1h3.5a1 1 0 0 1 1 1c0 1.25.2 2.45.57 3.57a1 1 0 0 1-.25 1z"/></symbol>
    <symbol id="i-fax" viewBox="0 0 24 24"><path d="M7 3h10v5H7zM4 9h16a2 2 0 0 1 2 2v6h-4v4H6v-4H2v-6a2 2 0 0 1 2-2zm4 7v3h8v-3z"/></symbol>
    <symbol id="i-mobile" viewBox="0 0 24 24"><path d="M8 1h8a2 2 0 0 1 2 2v18a2 2 0 0 1-2 2H8a2 2 0 0 1-2-2V3a2 2 0 0 1 2-2zm0 3v15h8V4zm4 16.2a1 1 0 1 0 0 .01z"/></symbol>
    <symbol id="i-mail" viewBox="0 0 24 24"><path d="M2 5h20v14H2zm2 2v.5l8 5.5 8-5.5V7zm0 3v7h16v-7l-8 5.5z"/></symbol>
    <symbol id="i-web" viewBox="0 0 24 24"><path d="M12 2a10 10 0 1 0 0 20 10 10 0 0 0 0-20zm-1 2.1V8H7.3A8 8 0 0 1 11 4.1zm2 0A8 8 0 0 1 16.7 8H13zM4.6 10h6.4v4H4.6a8 8 0 0 1 0-4zm8.4 0h6.4a8 8 0 0 1 0 4H13zm-5.7 6H11v3.9A8 8 0 0 1 7.3 16zm5.7 0h3.7A8 8 0 0 1 13 19.9z"/></symbol>
  </defs>
</svg>

<main class="sheet">
  <section class="card card--ko" aria-label="Korean side">
    <span class="card__rule"></span>
    <h1 class="card__person">최고경영자<br>박도현</h1>
    <div class="brand"><span class="brand__mark"></span>Corwell Insight Partners</div>
    <div class="card__contacts">
      <p class="contact-line">서울시 도봉구 매봉산로 82 한빛빌딩 507호</p>
      <p class="contact-line">
        <svg class="icon"><use href="#i-phone"/></svg>+82 2 718 4052<span class="gap"></span>
        <svg class="icon"><use href="#i-fax"/></svg>+82 2 864 1097<span class="gap"></span>
        <svg class="icon"><use href="#i-mobile"/></svg>+82 10 7264 8815
      </p>
      <p class="contact-line">
        <svg class="icon"><use href="#i-mail"/></svg>daniel@corwellip.com<span class="gap"></span>
        <svg class="icon"><use href="#i-web"/></svg>www.corwellip.com
      </p>
    </div>
  </section>

  <section class="card card--en" aria-label="English side">
    <span class="card__rule"></span>
    <h2 class="card__person">CEO<br>Daniel Park</h2>
    <div class="brand"><span class="brand__mark"></span>Corwell Insight Partners</div>
    <div class="card__contacts">
      <p class="contact-line">#507, Hanbit Bldg, 82 Maebongsan-ro,</p>
      <p class="contact-line">Dobong-gu, Seoul, 01327, Korea</p>
      <p class="contact-line">
        <svg class="icon"><use href="#i-phone"/></svg>+82 2 718 4052<span class="gap"></span>
        <svg class="icon"><use href="#i-fax"/></svg>+82 2 864 1097<span class="gap"></span>
        <svg class="icon"><use href="#i-mobile"/></svg>+82 10 7264 8815
      </p>
      <p class="contact-line">
        <svg class="icon"><use href="#i-mail"/></svg>daniel@corwellip.com<span class="gap"></span>
        <svg class="icon"><use href="#i-web"/></svg>www.corwellip.com
      </p>
    </div>
  </section>
</main>
</body>
</html>
```